Shipping Box & Supplies - Aquatics

Design shipping boxes and padded envelopes

Target Market(s)

Local Consumers

Industry/Entity Type

Tropical Fish/Aquatics

Requirements
Must have
• Logo, website and national telephone number
Nice to have
• Pictures attached
Should not have
• address

```html
<!DOCTYPE html>
<html lang="en">
<head>
<meta charset="utf-8">
<title>Reefhaven Aquatics – Envelope Set</title>
<link rel="stylesheet" href="https://fonts.googleapis.com/css2?family=Oswald:wght@500;600&display=swap">
<style>
  :root {
    --backdrop: #cbcfd0;
    --paper: #ffffff;
    --paper-shade: #eeeff1;
    --navy: #233b8b;
    --navy-soft: #2c4696;
    --white: #ffffff;
    --fold-line: #d6d7da;
  }
  * { margin: 0; padding: 0; box-sizing: border-box; }
  html, body {
    width: 1200px;
    height: 1200px;
    overflow: hidden;
    background: var(--backdrop);
  }
  .canvas {
    position: relative;
    width: 1200px;
    height: 1200px;
  }
  .envelope {
    position: absolute;
    left: 171px;
    width: 858px;
    background: linear-gradient(100deg, var(--paper) 0%, var(--paper) 35%, var(--paper-shade) 100%);
    overflow: hidden;
  }
  .envelope-front { top: 126px; height: 467px; }
  .envelope-back  { top: 696px; height: 367px; }

  .brand {
    position: absolute;
    left: 50%;
    top: 50%;
    transform: translate(-50%, -50%);
    display: flex;
    align-items: center;
    gap: 12px;
  }
  .brand-mark {
    width: 22px;
    height: 22px;
    background: var(--navy);
  }
  .brand-name {
    font-family: "Oswald", sans-serif;
    font-weight: 600;
    font-size: 30px;
    letter-spacing: 3px;
    color: var(--navy);
    text-transform: uppercase;
    white-space: nowrap;
  }

  .flap-outline {
    position: absolute;
    left: 0;
    top: 0;
    width: 858px;
    height: 110px;
  }
  .sea-band {
    position: absolute;
    left: 0;
    right: 0;
    top: 228px;
    bottom: 0;
    background: linear-gradient(180deg, var(--navy-soft) 0%, var(--navy) 100%);
  }
  .contact-line {
    position: absolute;
    left: 0;
    right: 0;
    top: 328px;
    text-align: center;
    font-family: "Oswald", sans-serif;
    font-weight: 500;
    font-size: 21px;
    letter-spacing: 1.5px;
    color: var(--white);
    white-space: nowrap;
  }
  .contact-divider { margin: 0 22px; }
</style>
</head>
<body>
<main class="canvas">

  <section class="envelope envelope-front" aria-label="Envelope front">
    <div class="brand">
      <span class="brand-mark"></span>
      <span class="brand-name">Reefhaven Aquatics</span>
    </div>
  </section>

  <section class="envelope envelope-back" aria-label="Envelope back">
    <svg class="flap-outline" viewBox="0 0 858 110" aria-hidden="true">
      <path d="M0 0 H858 L838 70 Q830 100 800 100 H60 Q28 100 20 70 Z"
            fill="none" stroke="var(--fold-line)" stroke-width="1.5"/>
    </svg>

    <div class="sea-band" role="img" aria-label="Navy ocean wave illustration with white bubbles along the bottom edge"></div>

    <p class="contact-line">
      <span class="contact-web">www.reefhavenaquatics.com</span><span class="contact-divider">|</span><span class="contact-phone">000-0000000000</span>
    </p>
  </section>

</main>
</body>
</html>
```